Velvet Pressings Techno Label Business Card

I'm looking for a very clean business card for my Velvet Pressings music label. The label focusses on techno music. The card should include:

• my name : Daniel Hovind as "Founder & CEO"
• email address: daniel@velvet-pressings.net
• web: www.velvet-pressings.net
• facebook logo + /velvetprs
• twitter logo + /velvetprs
• soundcloud logo + /velvetpressings

Feel free to include your ideas! I'm looking forward to discuss about it.

Daniel

Industry/Entity Type

Business

Contact Information for Business Card

I don't like glossy cards. Prefer matt.

Requirements
Nice to have
• Maybe on one side the complete logo, other side just the icon.
Should not have
• Flashy stuff. Must be clean and business like style.

```html
<!DOCTYPE html>
<html lang="en">
<head>
<meta charset="UTF-8">
<title>Velvet Pressings – Business Card</title>
<link rel="stylesheet" href="https://fonts.googleapis.com/css2?family=Cinzel:wght@700&family=Comfortaa:wght@500&family=Michroma&family=Open+Sans:wght@700&display=swap">
<style>
  :root {
    --backdrop: #e9e6e1;
    --card-top: #303030;
    --card-bottom: #262626;
    --accent: #f26522;
    --text-light: #f2f2f2;
    --text-muted: #8a8a8a;
  }
  * { margin: 0; padding: 0; box-sizing: border-box; }
  html, body {
    width: 1200px;
    height: 900px;
    overflow: hidden;
    background: var(--backdrop);
  }
  .sheet {
    width: 1200px;
    height: 900px;
    display: flex;
    flex-direction: column;
    align-items: center;
    justify-content: center;
    gap: 40px;
  }
  .card {
    position: relative;
    width: 660px;
    height: 390px;
    background: linear-gradient(180deg, var(--card-top) 0%, var(--card-bottom) 100%);
    overflow: hidden;
  }
  .card__band {
    position: absolute;
    left: 0; right: 0; bottom: 0;
    height: 24px;
    background: var(--accent);
  }

  /* Front side */
  .front__mark {
    position: absolute;
    inset: 0 0 24px 0;
    display: flex;
    align-items: center;
    justify-content: center;
    gap: 22px;
  }
  .front__dot {
    width: 54px;
    height: 54px;
    border-radius: 50%;
    background: var(--accent);
    flex: none;
  }
  .front__name {
    font-family: "Open Sans", Arial, sans-serif;
    font-weight: 700;
    font-size: 50px;
    color: var(--accent);
    letter-spacing: -0.5px;
    white-space: nowrap;
  }

  /* Back side */
  .back__label {
    position: absolute;
    top: 22px;
    left: 26px;
    display: flex;
    align-items: center;
    gap: 10px;
  }
  .back__dot {
    width: 28px;
    height: 28px;
    border-radius: 50%;
    background: var(--accent);
    flex: none;
  }
  .back__label-name {
    font-family: "Open Sans", Arial, sans-serif;
    font-weight: 700;
    font-size: 25px;
    color: var(--accent);
    letter-spacing: -0.3px;
    white-space: nowrap;
  }
  .back__person {
    position: absolute;
    top: 112px;
    left: 0; right: 0;
    text-align: center;
  }
  .back__name {
    font-family: "Michroma", Arial, sans-serif;
    font-weight: 400;
    font-size: 44px;
    color: var(--text-light);
    font-variant: small-caps;
    letter-spacing: 1px;
    line-height: 1.1;
    white-space: nowrap;
  }
  .back__title {
    margin-top: 2px;
    font-family: "Cinzel", Georgia, serif;
    font-weight: 700;
    font-size: 27px;
    color: var(--text-muted);
    letter-spacing: 2px;
    white-space: nowrap;
  }
  .back__social {
    position: absolute;
    left: 0; right: 0;
    top: 246px;
    display: flex;
    justify-content: center;
    gap: 30px;
    list-style: none;
    font-family: "Comfortaa", Arial, sans-serif;
    font-weight: 500;
    font-size: 15px;
    color: var(--text-muted);
  }
  .back__social-item {
    display: flex;
    align-items: center;
    gap: 8px;
    white-space: nowrap;
  }
  .back__social-marker {
    width: 14px;
    height: 14px;
    background: var(--accent);
    flex: none;
  }
  .back__contact {
    position: absolute;
    left: 26px; right: 26px;
    bottom: 36px;
    display: flex;
    justify-content: space-between;
    align-items: flex-end;
    font-family: "Comfortaa", Arial, sans-serif;
    font-weight: 500;
    font-size: 18px;
    color: var(--text-light);
    white-space: nowrap;
  }
  .back__email { margin-bottom: 14px; }
</style>
</head>
<body>
  <main class="sheet">
    <section class="card card--front" aria-label="Card front">
      <div class="front__mark">
        <span class="front__dot"></span>
        <span class="front__name">Velvet Pressings</span>
      </div>
      <div class="card__band"></div>
    </section>

    <section class="card card--back" aria-label="Card back">
      <div class="back__label">
        <span class="back__dot"></span>
        <span class="back__label-name">Velvet Pressings</span>
      </div>
      <div class="back__person">
        <h1 class="back__name">Daniel Hovind</h1>
        <p class="back__title">Founder &amp; CEO</p>
      </div>
      <ul class="back__social" aria-label="Social profiles">
        <li class="back__social-item"><span class="back__social-marker"></span>/velvetprs</li>
        <li class="back__social-item"><span class="back__social-marker"></span>/velvetprs</li>
        <li class="back__social-item"><span class="back__social-marker"></span>/velvetpressings</li>
      </ul>
      <div class="back__contact">
        <span class="back__email">daniel@velvet-pressings.net</span>
        <span class="back__web">www.velvet-pressings.net</span>
      </div>
      <div class="card__band"></div>
    </section>
  </main>
</body>
</html>
```